National online rug retailer needs a home page design

See the LoomNest logo and create a home page design around that color theme. Details are spelled out in word document uploaded below.
Updates

Apparently this website did not take my attachement showing the logo and basic requirements.  If you would send me your email address, I will send you the attachment directly.
Best regards,
Ned Carver
ncarver@qwplex.com

Target Market(s)

The target market is home owners 25 to 75 years old with combined incomes over $100,000 per year.

Industry/Entity Type

Online

Requirements
Must have
• Lots of white space with black letters and creative use of red and possibly one other color. Would like a compelling call to action button.

```html
<!DOCTYPE html>
<html lang="en">
<head>
<meta charset="utf-8">
<title>LoomNest – Home</title>
<link href="https://fonts.googleapis.com/css2?family=Open+Sans:wght@400;600;700;800&display=swap" rel="stylesheet">
<style>
:root{
  --red:#c8102e;
  --red-bright:#e01010;
  --ink:#222;
  --text:#444;
  --muted:#888;
  --line:#bbb;
  --panel:#eeeeee;
  --border:#c9c9c9;
  --green:#7bd32a;
}
*{box-sizing:border-box;margin:0;padding:0}
html,body{width:1120px;height:1200px;overflow:hidden;background:#fff;font-family:"Open Sans",Arial,sans-serif;color:var(--text)}
.page{position:relative;width:1120px;height:1200px}
.abs{position:absolute;white-space:nowrap}
a{color:inherit;text-decoration:none}

/* header */
.brand{left:168px;top:24px;display:flex;align-items:center;gap:8px}
.brand-mark{width:30px;height:30px;background:var(--red)}
.brand-name{font-size:26px;font-weight:600;color:var(--red);letter-spacing:-.5px}
.tagline{left:240px;top:69px;font-size:8px;color:var(--muted)}
.search{left:418px;top:39px;width:253px;height:39px;background:#e4e4e4;border:1px solid #d0d0d0;border-radius:3px;padding:5px}
.search-field{width:100%;height:27px;background:#fff;border:1px solid #ddd;display:flex;align-items:center;justify-content:space-between;padding-left:7px;font-size:11.5px;color:#333}
.search-btn{height:23px;margin-right:1px;padding:0 8px;background:var(--red-bright);color:#fff;font-size:12.5px;display:flex;align-items:center;gap:4px;border:1px solid #a00}
.cartline{left:698px;top:9px;width:250px;font-size:11px;line-height:15px;color:#555;padding-bottom:6px;border-bottom:1px dashed var(--line);text-align:right}
.cartline svg{vertical-align:-1px;margin-right:3px}
.cartline .red{color:var(--red)}
.cartline u{color:#222}
.tollfree{left:700px;top:39px;font-size:11px;line-height:15px;color:var(--muted)}
.tollfree svg{vertical-align:-1px}
.tollfree b{color:var(--red)}
.account{left:700px;top:63px;font-size:11.5px;color:#333}
.chat{left:822px;top:59px;width:123px;height:22px;background:#555;color:#fff;font-size:11.5px;display:flex;align-items:center;justify-content:center;gap:5px}
.chat span.on{color:var(--green)}

/* nav */
.nav{left:0;top:98px;width:1120px;height:30px;background:linear-gradient(#2a2a2a,#050505)}
.nav ul{list-style:none;display:flex;margin-left:160px;width:800px;height:30px;border-left:1px solid #333}
.nav li{flex:1;color:#fff;font-size:11.5px;display:flex;align-items:center;justify-content:center;border-right:1px solid #333}

/* sidebar */
.sidebar{left:167px;top:146px;width:170px;height:401px;border:1px solid var(--border);border-radius:2px;padding:12px 12px 0 13px}
.sidebar h3{color:var(--red);font-size:14.5px;font-weight:600;margin-bottom:5px}
.facet{font-size:10.5px;font-weight:700;color:var(--ink);height:24px;display:flex;align-items:center;gap:4px;border-bottom:1px dashed var(--line);margin-left:4px}
.facet.open{border-bottom:none}
.facet i{width:9px;height:9px;border-radius:50%;background:#555;color:#fff;font-style:normal;font-size:9px;line-height:9px;text-align:center;font-weight:700}
.facet-list{list-style:none;margin-left:4px;border-bottom:1px dashed var(--line)}
.facet-list li{height:24px;display:flex;align-items:center;padding-left:9px;font-size:11.5px;color:#333}
.facet-list li::before{content:"›";color:var(--red);margin-right:3px;font-weight:700}

/* promo bar */
.promo{left:353px;top:146px;width:599px;height:32px;border:1px solid var(--border);border-radius:2px;display:flex;align-items:center;padding-left:11px;gap:12px;box-shadow:inset 0 -2px 3px #eee;overflow:hidden}
.promo-title{font-size:19px;font-weight:700;color:#333}
.promo-title span{color:var(--red-bright);font-weight:600}
.promo-note{font-size:12px;color:#777}
.promo-note b{color:#555}

/* hero */
.hero{left:353px;top:193px;width:599px;height:205px;background:var(--panel);border:1px solid #d4d4d4;overflow:hidden}
.hero h2{position:absolute;left:19px;top:20px;font-size:30px;font-weight:700;color:#555;letter-spacing:.5px}
.hero h1{position:absolute;left:19px;top:55px;font-size:51px;font-weight:800;color:var(--red);letter-spacing:1px}
.hero p{position:absolute;left:23px;top:123px;font-size:14.5px;line-height:20px;color:#666}
.dots{position:absolute;left:24px;top:173px;display:flex;gap:7px}
.dots i{width:8px;height:8px;border-radius:50%;background:#ccc}
.dots i:first-child{background:#666}
.ribbon{position:absolute;right:0;bottom:0}

/* products */
.section-title{left:355px;top:413px;font-size:15px;font-weight:700;color:var(--red)}
.product{position:absolute;width:123px}
.product .img{height:176px;border:1px solid #ddd}
.product .name{font-size:11.5px;color:#333;margin-top:7px}
.product .price{font-size:11.5px;color:var(--red);margin-top:3px;padding-bottom:6px;border-bottom:1px dashed var(--line)}
.price s{color:var(--muted);margin-right:4px}

/* also like */
.also{left:800px;top:433px;width:154px;height:427px;border:1px solid var(--border);border-radius:2px}
.also h4{background:#e2e2e2;font-size:13.5px;font-weight:400;color:#444;padding:7px 7px;height:31px}
.also-item{display:flex;gap:9px;margin:0 7px;padding:9px 0 8px;border-bottom:1px dashed var(--line);height:78px}
.also-item .thumb{width:38px;height:58px;flex:none}
.also-item .t{font-size:11.5px;color:#333;line-height:19px;white-space:nowrap}
.also-item .t .price{color:var(--red)}
.also-item .t .more{color:var(--muted)}
.also-item .t .more b{color:var(--red)}

/* footer */
.footer{left:160px;top:960px;width:800px;height:190px;background:#ececec}
.fcol{position:absolute;top:19px}
.fcol h5{font-size:12px;font-weight:400;color:var(--red);margin-bottom:1px}
.fcol li{list-style:none;font-size:9.5px;color:#333;line-height:14.4px}
.pay{position:absolute;left:500px;top:40px;width:291px;height:101px;background:#fff;padding:10px 8px}
.pay .row{display:flex;gap:6px;justify-content:center;margin-bottom:10px}
.card{width:35px;height:22px;border-radius:2px}
.seal{height:40px;border-radius:4px}
.copy{position:absolute;left:503px;top:154px;font-size:11.5px;color:#555}
</style>
</head>
<body>
<div class="page">

  <header>
    <div class="abs brand"><span class="brand-mark"></span><span class="brand-name">LoomNest.com</span></div>
    <div class="abs tagline">for domestic and heirloom values</div>

    <div class="abs search">
      <div class="search-field">enter key words or item #
        <span class="search-btn">Search
          <svg width="11" height="11" viewBox="0 0 11 11"><circle cx="4.5" cy="4.5" r="3.3" fill="none" stroke="#fff" stroke-width="1.6"/><line x1="7" y1="7" x2="10" y2="10" stroke="#fff" stroke-width="1.8"/></svg>
        </span>
      </div>
    </div>

    <div class="abs cartline"><svg width="13" height="11" viewBox="0 0 13 11"><path d="M0 1h2.5l2 6h6.5l1.5-4.5H4" fill="none" stroke="#b00" stroke-width="1.4"/><circle cx="5.5" cy="9.5" r="1.2" fill="#b00"/><circle cx="10" cy="9.5" r="1.2" fill="#b00"/></svg>Items: <span class="red">0</span> | Total <span class="red">$0.00</span> | <u>View Cart</u> | <u>Checkout</u></div>
    <div class="abs tollfree">Order toll-free: <svg width="11" height="11" viewBox="0 0 11 11"><rect width="11" height="11" rx="2" fill="#999"/><path d="M3 2.5c0 3 2.5 6 5.5 6l.5-1.5-1.5-1-1 .8c-.8-.4-1.5-1.1-1.8-1.8l.8-1-1-1.5z" fill="#fff"/></svg> <b>1-888-555-0142</b></div>
    <div class="abs account">My Account &nbsp;|&nbsp; Sign In</div>
    <div class="abs chat">Live Chat
      <svg width="16" height="12" viewBox="0 0 16 12"><ellipse cx="6" cy="5" rx="6" ry="4.5" fill="#7bd32a"/><path d="M2 8l-1 3 4-2z" fill="#7bd32a"/><ellipse cx="11" cy="7" rx="4.5" ry="3.5" fill="#5fb01f"/></svg>
      <span class="on">ONLINE</span></div>
  </header>

  <nav class="abs nav">
    <ul>
      <li>Home</li><li>Selection guides</li><li>Rug Care</li><li>FAQ</li><li>Return Policy</li><li>Free Shipping</li><li>Clearance Rugs</li>
    </ul>
  </nav>

  <aside class="abs sidebar">
    <h3>Browse</h3>
    <div class="facet open"><i>–</i>RUG THEME</div>
    <ul class="facet-list"><li>Traditional</li><li>Transitional</li><li>Casual</li></ul>
    <div class="facet open"><i>–</i>COLOR WAY</div>
    <ul class="facet-list"><li>Black</li><li>Blue</li><li>Green</li><li>Gold</li></ul>
    <div class="facet"><i>+</i>SIZE</div>
    <div class="facet"><i>+</i>SHAPE</div>
    <div class="facet"><i>+</i>FIBER CONTENT</div>
    <div class="facet"><i>+</i>MFGR. BRAND</div>
    <div class="facet"><i>+</i>MFGR.COLLECTION</div>
    <div class="facet"><i>+</i>PRICE</div>
  </aside>

  <div class="abs promo">
    <div class="promo-title"><span>20% OFF</span> ON HARLOW MILLS RUGS</div>
    <div class="promo-note"><b>Hurry up!</b> The Sale will expire on 5th July</div>
  </div>

  <section class="abs hero">
    <h2>FATHER’S DAY SALE</h2>
    <h1>UPTO EXTRA 50% OFF</h1>
    <p>All rugs. Take an Additional 10% OFF<br>Refer 3 friends and get Another 5% Off</p>
    <div class="dots"><i></i><i></i><i></i><i></i><i></i></div>
    <svg class="ribbon" width="100" height="100" viewBox="0 0 100 100">
      <polygon points="100,12 100,48 48,100 12,100" fill="#dcdcdc"/>
      <polygon points="100,48 100,100 48,100" fill="#f4f4f4"/>
      <text x="62" y="68" transform="rotate(-45 62 68)" text-anchor="middle" font-family="Open Sans,sans-serif" font-size="12" font-weight="600" fill="#c8102e">Ends Monday</text>
    </svg>
  </section>

  <div class="abs section-title">RUGS</div>

  <div class="product" style="left:354px;top:434px">
    <div class="img" role="img" aria-label="Striped red rug with orange lettering" style="background:linear-gradient(90deg,#b9473a,#d98c5a,#a84a3f)"></div>
    <div class="name">Fusce facilisi</div><div class="price"><s>$200</s>$114</div>
  </div>
  <div class="product" style="left:506px;top:434px">
    <div class="img" role="img" aria-label="Lilac and grey petal pattern rug" style="background:linear-gradient(135deg,#b79cc0,#9a8f92,#a77cbc)"></div>
    <div class="name">Sed vitae</div><div class="price"><s>$200</s>$120</div>
  </div>
  <div class="product" style="left:654px;top:434px">
    <div class="img" role="img" aria-label="Red rug with orange triangles" style="background:linear-gradient(135deg,#e03a22,#f07a35,#d9261b)"></div>
    <div class="name">Donec urna</div><div class="price"><s>$120</s>$100</div>
  </div>
  <div class="product" style="left:357px;top:682px">
    <div class="img" role="img" aria-label="Red rug with round medallion" style="background:radial-gradient(circle,#e08a6a 0,#d9322a 22%,#d41f1f 60%)"></div>
    <div class="name">Praesent eros</div><div class="price">$234</div>
  </div>
  <div class="product" style="left:506px;top:682px">
    <div class="img" role="img" aria-label="Pink and grey petal pattern rug" style="background:linear-gradient(135deg,#ec8fb6,#b7a7ab,#e46fa0)"></div>
    <div class="name">Vestibulum tristique</div><div class="price">$250</div>
  </div>
  <div class="product" style="left:654px;top:682px">
    <div class="img" role="img" aria-label="Shaggy grey and olive striped rug" style="background:linear-gradient(180deg,#6d7664,#8a8f63,#5e6670)"></div>
    <div class="name">Maecenas id dictum</div><div class="price">$540</div>
  </div>

  <aside class="abs also">
    <h4>You may also Like</h4>
    <div class="also-item"><div class="thumb" role="img" aria-label="Dark red patterned rug" style="background:#8c1f2a"></div>
      <div class="t">Aenean vestibul<br><span class="price"><s>$200</s>$114</span><br><span class="more">View Details <b>›</b></span></div></div>
    <div class="also-item"><div class="thumb" role="img" aria-label="Green rug" style="background:#97bd74"></div>
      <div class="t">Donec interdum<br><span class="price"><s>$300</s>$194</span><br><span class="more">View Details <b>›</b></span></div></div>
    <div class="also-item"><div class="thumb" role="img" aria-label="Orange red rug" style="background:#d9401f"></div>
      <div class="t">Vivamus imperd<br><span class="price"><s>$456</s>$320</span><br><span class="more">View Details <b>›</b></span></div></div>
    <div class="also-item"><div class="thumb" role="img" aria-label="Brown striped rug" style="background:linear-gradient(#4a2a22,#b59b86,#4a2a22)"></div>
      <div class="t">Sed placerat<br><span class="price"><s>$350</s>$240</span><br><span class="more">View Details <b>›</b></span></div></div>
    <div class="also-item"><div class="thumb" role="img" aria-label="Pink rug" style="background:#d9788a"></div>
      <div class="t">Maecenas ac<br><span class="price"><s>$370</s>$280</span><br><span class="more">View Details <b>›</b></span></div></div>
  </aside>

  <footer class="abs footer">
    <div class="fcol" style="left:14px"><h5>Customer Service</h5><ul><li>Shipping</li><li>Return Policy</li><li>Privacy Policy</li><li>Ordering &amp; Delivery Checklist</li><li>Terms of Use</li><li>Terms of Sale</li><li>Contact Us</li><li>Environmental Policy</li></ul></div>
    <div class="fcol" style="left:191px"><h5>Resources</h5><ul><li>Product Articles</li><li>Learning Center</li><li>Help</li><li>Refer A Friend</li><li>LoomNest Blog</li><li>Room Scene Viewer</li><li>Site Map</li><li>FAQ</li><li>Customer Testimonials</li><li>Photo Gallery</li></ul></div>
    <div class="fcol" style="left:350px"><h5>Corporate Info</h5><ul><li>About LoomNest.com</li><li>Careers</li><li>Affiliates</li></ul></div>
    <div class="fcol" style="left:500px"><h5>Payment and Security</h5></div>
    <div class="pay">
      <div class="row">
        <span class="card" style="background:#2a4a9a"></span><span class="card" style="background:#e0a030"></span><span class="card" style="background:#e6e6e6"></span><span class="card" style="background:#5a8fd0"></span><span class="card" style="background:#d7e3f2"></span><span class="card" style="background:#dde4ec"></span>
      </div>
      <div class="row" style="align-items:center">
        <span class="seal" style="width:36px;border-radius:50%;background:#b9a23a"></span><span class="seal" style="width:40px;border-radius:50%;background:#e8c640"></span><span class="seal" style="width:54px;height:24px;background:#e3e3e3"></span><span class="seal" style="width:50px;height:28px;background:#2c5aa0"></span><span class="seal" style="width:62px;height:28px;background:#2b2b2b"></span>
      </div>
    </div>
    <div class="copy">Copyright © 2013 LoomNest.com. All rights reserved</div>
  </footer>

</div>
</body>
</html>
```